2 Wine Label Designs

Vintner Bloom has been helping people give customized wine gifts since 1999. From large scale corporate clients, to 1 bottle personalized gifts, we offer a wide range of wines and templates for any occasion. Recently we’ve started to shift our focus to a younger demographic (21 to 35 year old women) and are in the process of updating our website and branding.

One big area we’re working to improve is the customizable wine label/engraving templates we offer on the site (to see our current template library go to www.vintnerbloom-demo.com/shop/wine, select a wine, choose “label” or “engraving” from the dropdown, and click “customize”). You’ll find that a lot of our current templates are outdated or aimed at an older demographic. Over the next few months we want to swap out most of these old templates with fun fresh designs.

We're asking designers to submit 2 customizable wine label templates for this project. One should be wedding themed and the other "Thank You" themed. Please see the attached PDF for more guidelines and creative direction.

Keep in mind, even if you aren't selected as the winner of this project we are going to go through and offer $50 for any label template submitted that we like ($100 if we want both). So there is a good chance you'll be getting some money for your work!

Please read though the attached guidelines PDF carefully (especially the "Must be Customizable" section).

Target Market(s)

21 to 35 year old women

Colors

Designer to choose colors to be used in the design.

Requirements
Must have
• See attached PDF
Nice to have
• See attached PDF
Should not have
• See attached PDF

```html
<!DOCTYPE html>
<html lang="en">
<head>
<meta charset="utf-8">
<title>Thank You Wine Label – Vintner Bloom Template</title>
<link rel="stylesheet" href="https://fonts.googleapis.com/css2?family=Cinzel:wght@400&family=Dancing+Script:wght@500&family=Playball&family=Josefin+Sans:wght@400&display=swap">
<style>
  :root {
    --parchment-light: #e6dcc6;
    --parchment-mid: #d2c5a6;
    --parchment-dark: #b7a582;
    --floral-deep: #5a3a24;
    --floral-warm: #8b6a48;
    --floral-soft: #b59a74;
    --ink: #15120f;
  }
  html, body {
    margin: 0;
    padding: 0;
    width: 1200px;
    height: 900px;
    overflow: hidden;
    background: var(--parchment-light);
  }
  .label {
    position: relative;
    width: 1200px;
    height: 900px;
    overflow: hidden;
    background:
      radial-gradient(ellipse at 50% 40%, var(--parchment-light) 0%, var(--parchment-mid) 60%, var(--parchment-dark) 100%);
  }
  .floral {
    position: absolute;
    border-radius: 50%;
    filter: blur(6px);
  }
  .floral--top-left {
    left: -120px; top: -80px; width: 420px; height: 380px;
    background: radial-gradient(ellipse at 35% 40%, var(--floral-deep) 0%, var(--floral-warm) 40%, rgba(139,106,72,0) 72%);
  }
  .floral--bottom-left {
    left: -110px; top: 620px; width: 380px; height: 380px;
    background: radial-gradient(ellipse at 30% 55%, var(--floral-warm) 0%, var(--floral-soft) 40%, rgba(181,154,116,0) 72%);
  }
  .floral--right {
    left: 1000px; top: 40px; width: 320px; height: 720px;
    background: radial-gradient(ellipse at 60% 50%, var(--floral-deep) 0%, var(--floral-warm) 38%, rgba(139,106,72,0) 72%);
  }
  .floral--bottom-centre {
    left: 840px; top: 790px; width: 360px; height: 200px;
    background: radial-gradient(ellipse at 50% 60%, var(--floral-deep) 0%, rgba(90,58,36,0) 70%);
  }
  .text {
    position: absolute;
    margin: 0;
    color: var(--ink);
    white-space: nowrap;
    line-height: 1;
    text-shadow: 1px 2px 3px rgba(0,0,0,0.25);
  }
  .thank-you {
    left: 0; width: 1200px; top: 72px;
    text-align: center;
    font-family: "Cinzel", serif;
    font-size: 96px;
    letter-spacing: 3px;
  }
  .intro-line {
    left: 0; width: 1200px; top: 186px;
    text-align: center;
    font-family: "Cinzel", serif;
    font-size: 44px;
    letter-spacing: 1px;
  }
  .script {
    font-family: "Dancing Script", cursive;
    font-weight: 500;
  }
  .script--best { left: 588px; top: 258px; font-size: 88px; }
  .script--day { left: 362px; top: 250px; font-size: 210px; }
  .script--ever { left: 528px; top: 440px; font-size: 158px; }
  .couple-title {
    left: 0; width: 1200px; top: 612px;
    text-align: center;
    font-family: "Playball", cursive;
    font-size: 58px;
  }
  .couple-name {
    left: 0; width: 1200px; top: 684px;
    text-align: center;
    font-family: "Playball", cursive;
    font-size: 66px;
  }
  .wedding-date {
    left: 0; width: 1200px; top: 790px;
    text-align: center;
    font-family: "Josefin Sans", sans-serif;
    font-size: 40px;
    letter-spacing: 4px;
  }
</style>
</head>
<body>
  <main class="label">
    <div class="floral floral--top-left" role="img" aria-label="Vintage sepia floral branch in the top left corner"></div>
    <div class="floral floral--bottom-left" role="img" aria-label="Faded sepia lily blossoms in the bottom left corner"></div>
    <div class="floral floral--right" role="img" aria-label="Cascading vintage roses and leaves along the right edge"></div>
    <div class="floral floral--bottom-centre" role="img" aria-label="Dark sepia leaves along the bottom edge"></div>

    <h1 class="text thank-you">Thank You</h1>
    <p class="text intro-line">For being Part of Our</p>
    <p class="text script script--day">Day</p>
    <p class="text script script--best">Best</p>
    <p class="text script script--ever">Ever</p>
    <p class="text couple-title">Mr &amp; Mrs</p>
    <p class="text couple-name">Marwell</p>
    <p class="text wedding-date">09.09.2018</p>
  </main>
</body>
</html>
```